Northgate Print and Paper Business

Hi, I need template designs for stationary as listed below using my Logo as per attached file;
1) Business Card (double sided)
2) Letterhead
3) With Compliments Slip
4) Return Address Label (Stickers)

```html
<!DOCTYPE html>
<html lang="en">
<head>
<meta charset="utf-8">
<title>Return Address Label – Northgate Print and Paper Business</title>
<link rel="stylesheet" href="https://fonts.googleapis.com/css2?family=Mulish:wght@400;700&display=swap">
<style>
  :root {
    --backdrop: #ececec;
    --paper: #ffffff;
    --edge: #dcdcdc;
    --ink: #2a2a2a;
    --magenta: #d8127e;
    --green: #2e8f3e;
    --faint-green: #dcebd8;
    --faint-pink: #f6d3e6;
  }
  * { margin: 0; padding: 0; box-sizing: border-box; }
  html, body {
    width: 1200px;
    height: 900px;
    overflow: hidden;
    background: var(--backdrop);
    font-family: "Mulish", sans-serif;
    color: var(--ink);
  }
  .label {
    position: absolute;
    left: 180px;
    top: 312px;
    width: 840px;
    height: 276px;
    background: var(--paper);
    border: 1px solid var(--edge);
    overflow: hidden;
  }
  .brand {
    position: absolute;
    left: 48px;
    top: 96px;
    display: flex;
    align-items: center;
    gap: 14px;
  }
  .brand-dot {
    width: 26px;
    height: 26px;
    border-radius: 50%;
    background: var(--magenta);
    flex: none;
  }
  .brand-name {
    font-weight: 700;
    font-size: 30px;
    line-height: 34px;
    color: var(--ink);
  }
  .address {
    position: absolute;
    left: 352px;
    top: 104px;
    font-style: normal;
  }
  .address-name {
    font-weight: 700;
    font-size: 27px;
    line-height: 36px;
    letter-spacing: 0.2px;
  }
  .address-line {
    font-weight: 400;
    font-size: 19px;
    line-height: 26px;
  }
  .corner-accent {
    position: absolute;
    right: 0;
    bottom: 0;
  }
</style>
</head>
<body>
  <section class="label">
    <div class="brand">
      <span class="brand-dot"></span>
      <span class="brand-name">Northgate<br>Print and Paper</span>
    </div>

    <address class="address">
      <div class="address-name">Helen Darcy</div>
      <div class="address-line">Northgate Print and Paper Business</div>
      <div class="address-line">PO Box 208</div>
      <div class="address-line">Larkfield NSW 2099</div>
      <div class="address-line">Australia</div>
    </address>

    <svg class="corner-accent" width="200" height="230" viewBox="0 0 200 230" aria-hidden="true">
      <circle cx="150" cy="190" r="120" fill="var(--faint-pink)" opacity="0.55"/>
    </svg>
  </section>
</body>
</html>
```